Payday Lending App Interface Design

Hello, we are building a payday lending application, Lendora, that lend people money. I have drafted some of the screens that show the functionalities we have at the moment, please find the screens in attachments.
The elements in the screens are placed just to show what should be included in those screens, it's not necessary to follow the same layout. If you have better design ideas, you are very welcomed to show off your talent.
I think what we want is a style guide so that we can apply the same style to any screens that are similar to the ones I attached. We really like
the style as in the attached image called Style.png. We might want something similar - a simple, clean design yet fun and engaging. Customised graphical elements such as icons, illustrations are preferable.
Apart from the attached screens, we might also need a design for the On Board screen and the Login/Sign Up screen too.
Our logo colour is in yellow and black. Perhaps we will have a similar colour theme. I also attached the logo file, icon-Lendora.png, if you would like to put it in your design.
Please message me if you need further information.
Regards
Target Market(s)
Young people that doesn't have strong income
Look and feel

```html
<!DOCTYPE html>
<html lang="en">
<head>
<meta charset="UTF-8">
<title>Lendora – Loan Details</title>
<link href="https://fonts.googleapis.com/css2?family=Mulish:wght@400;600;700;800&family=Roboto:wght@400;500;700&display=swap" rel="stylesheet">
<style>
  :root {
    --brand-yellow: #f9d20b;
    --ink: #0d0d0d;
    --ink-soft: #7a6a06;
    --sheet: #ffffff;
    --track: #e2e2e2;
    --muted: #8a8a8a;
    --divider: #d9d9d9;
    --page: #ffffff;
  }
  * { margin: 0; padding: 0; box-sizing: border-box; }
  html, body {
    width: 1200px;
    height: 2597px;
    overflow: hidden;
    background: var(--page);
  }
  .screen {
    position: relative;
    width: 1200px;
    height: 2597px;
    overflow: hidden;
    background: var(--page);
  }
  .hero {
    position: absolute;
    left: 0; top: 0;
    width: 1200px;
    height: 1260px;
    background: var(--brand-yellow);
    border-radius: 116px 116px 0 0;
    font-family: "Mulish", sans-serif;
    text-align: center;
  }
  .back-button {
    position: absolute;
    left: 98px; top: 112px;
    width: 60px; height: 64px;
  }
  .hero-title {
    position: absolute;
    left: 0; right: 0; top: 286px;
    font-size: 100px;
    font-weight: 800;
    line-height: 1;
    color: var(--ink);
  }
  .hero-subtitle {
    position: absolute;
    left: 0; right: 0; top: 416px;
    font-size: 66px;
    font-weight: 600;
    line-height: 1;
    color: var(--ink-soft);
  }
  .amount {
    position: absolute;
    left: 0; right: 0; top: 580px;
    display: flex;
    justify-content: center;
    align-items: flex-start;
    color: var(--ink);
    font-weight: 800;
  }
  .amount-currency {
    font-size: 116px;
    line-height: 1;
    margin-top: 10px;
    margin-right: 28px;
  }
  .amount-value {
    font-size: 240px;
    line-height: 0.9;
    letter-spacing: -4px;
  }
  .due-date {
    position: absolute;
    left: 0; right: 0; top: 906px;
    font-size: 76px;
    font-weight: 600;
    line-height: 1;
    color: var(--ink-soft);
  }
  .sheet {
    position: absolute;
    left: 0; top: 1124px;
    width: 1200px;
    height: 1473px;
    background: var(--sheet);
    border-radius: 116px 116px 0 0;
    font-family: "Roboto", sans-serif;
  }
  .sheet-handle {
    position: absolute;
    left: 548px; top: 58px;
    width: 122px; height: 14px;
    border-radius: 7px;
    background: var(--track);
  }
  .progress {
    position: absolute;
    left: 136px; top: 184px;
    width: 925px; height: 130px;
    border-radius: 65px;
    background: var(--track);
    overflow: hidden;
  }
  .progress-paid {
    position: absolute;
    left: 0; top: 0;
    width: 595px; height: 130px;
    border-radius: 65px;
    background: var(--brand-yellow);
  }
  .progress-label {
    position: absolute;
    top: 0;
    height: 130px;
    line-height: 130px;
    font-size: 46px;
    color: var(--ink);
    text-align: center;
  }
  .progress-label.paid { left: 0; width: 595px; }
  .progress-label.left { left: 595px; width: 330px; }
  .progress-caption {
    position: absolute;
    top: 344px;
    font-size: 42px;
    line-height: 1;
    color: var(--ink);
  }
  .progress-caption.paid { left: 148px; }
  .progress-caption.left { right: 176px; }
  .progress-percent {
    position: absolute;
    left: 500px; width: 200px; top: 352px;
    text-align: center;
    font-family: "Mulish", sans-serif;
    font-size: 64px;
    font-weight: 800;
    line-height: 1;
    color: var(--brand-yellow);
  }
  .activities-title {
    position: absolute;
    left: 136px; top: 646px;
    font-size: 82px;
    font-weight: 700;
    line-height: 1;
    color: var(--ink);
  }
  .activity {
    position: absolute;
    left: 93px;
    width: 1012px;
    height: 270px;
    border-bottom: 3px solid var(--divider);
  }
  .activity-type {
    position: absolute;
    left: 43px; top: 0;
    font-size: 54px;
    line-height: 1;
    color: var(--ink);
  }
  .activity-date {
    position: absolute;
    left: 43px; top: 92px;
    font-size: 50px;
    line-height: 1;
    color: var(--muted);
  }
  .activity-amount {
    position: absolute;
    right: 112px; top: 0;
    font-size: 54px;
    line-height: 1;
    color: var(--ink);
  }
</style>
</head>
<body>
<main class="screen">
  <header class="hero">
    <svg class="back-button" viewBox="0 0 60 64" aria-label="Back">
      <polyline points="40,10 18,32 40,54" fill="none" stroke="#6b5a06" stroke-width="9" stroke-linecap="round" stroke-linejoin="round"/>
    </svg>
    <h1 class="hero-title">Loan Details</h1>
    <p class="hero-subtitle">Next Repayment</p>
    <div class="amount">
      <span class="amount-currency">$</span>
      <span class="amount-value">50</span>
    </div>
    <p class="due-date">On 4 Dec</p>
  </header>

  <section class="sheet">
    <div class="sheet-handle"></div>

    <div class="progress">
      <div class="progress-paid"></div>
      <span class="progress-label paid">XXX</span>
      <span class="progress-label left">XX</span>
    </div>
    <span class="progress-caption paid">Paid</span>
    <span class="progress-percent">60%</span>
    <span class="progress-caption left">Left</span>

    <h2 class="activities-title">Activities</h2>

    <div class="activity" style="top: 848px;">
      <span class="activity-type">Repayment</span>
      <span class="activity-date">dd/mm/yyyy</span>
      <span class="activity-amount">$XX</span>
    </div>
    <div class="activity" style="top: 1118px; height: 226px;">
      <span class="activity-type">Repayment</span>
      <span class="activity-date">dd/mm/yyyy</span>
      <span class="activity-amount">$XX</span>
    </div>
  </section>
</main>
</body>
</html>
```